Church Christmas Flyer

The flyer is to advertise our Christmas Eve services. The flyer is for a Christian church service to celebrate the birth of Jesus. We would like to see designs that use blue, silver and gold for colors but feel free to be creative. We are interested in a flyer that is has texture, depth and is more abstract than literal. Don't be afraid to layer. Please make the flyer double sided

* I uploaded our Christmas flyer from last year.

Target Market(s)

30-55 year old, male and female

Industry/Entity Type

Church

Requirements
Must have
• Map to the church
Church phone number 555-314-7096
Service times 3:00pm and 5:00pm
church address 28315 Marigold Ave, Hesperia, Ca. 92345
church website www.brookstonefellowship.example
Scripture verse

Text must stand out and be easy to read
Nice to have
• Use of the star in the sky that guided the wise men to Jesus.
Should not have
• Santa Clause, Snowmen, Reindeer

```html
<!DOCTYPE html>
<html lang="en">
<head>
<meta charset="utf-8">
<title>Christmas Eve – A Celebration of God's Love</title>
<link rel="stylesheet" href="https://fonts.googleapis.com/css2?family=Roboto+Condensed:wght@300;400;700&family=Roboto:wght@300;400;500&display=swap">
<style>
  :root {
    --stage: #2a2126;
    --violet-deep: #1f0a2a;
    --violet: #4a1f78;
    --violet-mid: #6a3a9a;
    --ice: #9fe3f2;
    --white: #ffffff;
    --soft-white: rgba(255,255,255,0.82);
  }
  * { margin: 0; padding: 0; box-sizing: border-box; }
  html, body { width: 1200px; height: 1079px; overflow: hidden; }
  body { background: var(--stage); position: relative; font-family: "Roboto", Arial, sans-serif; color: var(--white); }

  .rack-card {
    position: absolute; top: 67px; width: 418px; height: 944px; overflow: hidden;
    background:
      radial-gradient(circle at 30% 18%, rgba(210,200,255,0.55) 0 14%, transparent 30%),
      radial-gradient(circle at 78% 6%, rgba(127,214,240,0.7) 0 8%, transparent 26%),
      radial-gradient(circle at 25% 32%, rgba(200,180,240,0.45) 0 18%, transparent 34%),
      radial-gradient(circle at 80% 30%, rgba(190,170,235,0.35) 0 12%, transparent 28%),
      linear-gradient(180deg, #5fb8e4 0%, #6b5fc4 14%, var(--violet-mid) 32%, var(--violet) 52%, #33154f 70%, var(--violet-deep) 100%);
  }
  .card-front { left: 152px; }
  .card-back { left: 639px; }

  .card-layer { position: absolute; inset: 0; width: 100%; height: 100%; }

  /* Front title lockup */
  .title-lockup text { fill: var(--white); font-family: "Roboto Condensed", "Arial Narrow", sans-serif; }
  .title-christmas { font-size: 64px; font-weight: 700; }
  .title-eve { font-size: 190px; font-weight: 700; }
  .tagline-top { font-size: 34px; font-weight: 300; }
  .tagline-bottom { font-size: 52px; font-weight: 300; }

  /* Back */
  .scripture { position: absolute; inset: 0; font-weight: 300; color: var(--soft-white); }
  .scripture span { position: absolute; white-space: nowrap; line-height: 1; }
  .scripture b { font-weight: 500; color: var(--white); }
  .quote-mark { font: 700 64px/1 Georgia, serif; color: var(--white); }
  .quote-open { left: 4px; top: 38px; }
  .quote-close { left: 350px; top: 236px; }
  .verse-1 { left: 38px; top: 56px; font-size: 26px; }
  .verse-2 { left: 38px; top: 84px; font-size: 29px; }
  .verse-3 { left: 124px; top: 118px; font-size: 24px; }
  .verse-4 { left: 38px; top: 140px; font-size: 46px; }
  .verse-5 { left: 228px; top: 182px; font-size: 27px; }
  .verse-6 { left: 82px; top: 200px; font-size: 56px; }

  .section-heading {
    position: absolute; left: 44px;
    font: 700 27px/1 "Roboto Condensed", "Arial Narrow", sans-serif; color: var(--ice);
  }
  .heading-times { top: 352px; }
  .heading-address { top: 566px; }
  .detail-line { position: absolute; left: 44px; font-size: 20px; line-height: 1; white-space: nowrap; }
  .detail-line.strong { font-weight: 500; }
  .detail-line.muted { color: var(--soft-white); font-weight: 400; }
  .detail-line .plain { font-weight: 400; }

  .divider { position: absolute; left: 0; top: 532px; width: 418px; height: 20px; }

  .map-area {
    position: absolute; left: 50px; top: 674px; width: 250px; height: 204px; border-radius: 4px;
    background: radial-gradient(ellipse at 55% 65%, rgba(160,120,210,0.35), rgba(40,14,60,0.25) 70%, transparent);
  }

  .contact-footer {
    position: absolute; left: 0; right: 0; top: 912px; text-align: center;
    font-size: 13.5px; letter-spacing: 1px; color: var(--soft-white); font-weight: 300;
  }
  .contact-footer .sep { margin: 0 14px; }
</style>
</head>
<body>

<section class="rack-card card-front" aria-label="Flyer front">
  <svg class="card-layer" viewBox="0 0 418 944" aria-hidden="true">
    <polygon points="0,660 418,300 418,330 0,720" fill="rgba(255,255,255,0.05)"/>
    <polygon points="0,780 240,944 180,944 0,830" fill="rgba(255,255,255,0.08)"/>
    <polygon points="0,860 110,760 150,780 40,944 0,944" fill="rgba(255,255,255,0.10)"/>
    <line x1="0" y1="905" x2="150" y2="760" stroke="rgba(255,255,255,0.55)" stroke-width="1.5"/>
    <line x1="20" y1="944" x2="418" y2="860" stroke="rgba(255,255,255,0.25)" stroke-width="1"/>
    <polygon points="300,860 418,830 418,944 360,944" fill="rgba(255,255,255,0.07)"/>
    <line x1="300" y1="944" x2="418" y2="880" stroke="rgba(255,255,255,0.45)" stroke-width="1.5"/>
  </svg>

  <svg class="card-layer title-lockup" viewBox="0 0 418 944" role="img" aria-label="Christmas Eve – A Celebration of God's Love">
    <g class="guiding-star">
      <circle cx="231" cy="530" r="8" fill="rgba(255,255,255,0.5)"/>
      <polygon points="231,500 233,528 261,530 233,532 231,560 229,532 201,530 229,528" fill="#fff"/>
    </g>
    <text class="title-christmas" x="139" y="596" textLength="236" lengthAdjust="spacingAndGlyphs">CHRISTMAS</text>
    <text class="title-eve" x="139" y="742" textLength="237" lengthAdjust="spacingAndGlyphs">EVE</text>
    <line x1="104" y1="762" x2="418" y2="762" stroke="rgba(255,255,255,0.55)" stroke-width="1"/>
    <text class="tagline-top" x="139" y="809" textLength="236" lengthAdjust="spacingAndGlyphs">A CELEBRATION OF</text>
    <text class="tagline-bottom" x="139" y="855" textLength="236" lengthAdjust="spacingAndGlyphs">GOD'S LOVE</text>
  </svg>
</section>

<section class="rack-card card-back" aria-label="Flyer back">
  <div class="scripture">
    <span class="quote-mark quote-open">“</span>
    <span class="verse-1">He will be great, and</span>
    <span class="verse-2"><b>will be called the Son</b></span>
    <span class="verse-3">of the <b>Highest</b>... and of</span>
    <span class="verse-4"><b>His kingdom</b></span>
    <span class="verse-5">there will</span>
    <span class="verse-6">be no end.</span>
    <span class="quote-mark quote-close">”</span>
  </div>

  <h2 class="section-heading heading-times">SERVICE TIMES</h2>
  <p class="detail-line strong" style="top:392px">3:00PM and 5:00PM</p>
  <p class="detail-line muted" style="top:415px">Sat. December 24, 2011</p>
  <p class="detail-line strong" style="top:446px">8:30AM and 10:30AM</p>
  <p class="detail-line muted" style="top:470px">Sun. December 25, 2011</p>

  <svg class="divider" viewBox="0 0 418 20" aria-hidden="true">
    <line x1="0" y1="10" x2="56" y2="10" stroke="rgba(255,255,255,0.5)"/>
    <line x1="94" y1="10" x2="418" y2="10" stroke="rgba(255,255,255,0.5)"/>
    <path d="M62 10 C66 3 72 3 75 10 C78 17 84 17 88 10" fill="none" stroke="#fff" stroke-width="2"/>
  </svg>

  <h2 class="section-heading heading-address">ADDRESS</h2>
  <p class="detail-line strong" style="top:600px">28315 Marigold Ave, <span class="plain">Hesperia,</span></p>
  <p class="detail-line" style="top:623px">Ca. 92345</p>

  <div class="map-area" role="img" aria-label="Street map showing the way to the church"></div>

  <p class="contact-footer">555-314-7096<span class="sep">|</span>www.brookstonefellowship.example</p>
</section>

</body>
</html>
```